Marlow Hire Business Card for recruitment company

We are looking for a Business Card Design that incorporates our personal details and our busines name and logo. We are a specialized search consultancy that recruit Property and Construction professionals.
We would like a business card that stands out and is appealing to the Construction and Property industry as well.

Target Market(s)

people in the construction and property industry

Contact Information for Business Card

Business Name and logo

Font styles to use
Serif

Colors
0094D4
00A9DD
6FCCEA
C7EBF8
E9F6FB

Requirements
Must have
• Business name and logo as well as contact details
Should not have
• No photos of us please

```html
<!DOCTYPE html>
<html lang="en">
<head>
<meta charset="utf-8">
<title>Marlow Hire – Business Card</title>
<link rel="stylesheet" href="https://fonts.googleapis.com/css2?family=Jost:wght@300;400&family=Source+Sans+3:wght@300;700&family=Poppins:wght@600&display=swap">
<style>
  :root {
    --backdrop: #c9c9c9;
    --navy: #033649;
    --white: #ffffff;
    --muted: #8a8a8a;
    --ghost: #e4e4e4;
  }
  * { margin: 0; padding: 0; box-sizing: border-box; }
  html, body { width: 1200px; height: 1000px; overflow: hidden; }
  body { background: var(--backdrop); position: relative; }

  .card { position: absolute; overflow: hidden; }

  .card-back {
    left: 95px; top: 107px; width: 621px; height: 372px;
    background: var(--navy);
  }
  .card-back .wordmark {
    position: absolute; right: 19px; top: 285px;
    color: var(--white);
  }

  .wordmark {
    font-family: "Jost", sans-serif;
    font-weight: 300;
    font-size: 30px;
    letter-spacing: 1px;
    line-height: 1;
    white-space: nowrap;
  }

  .card-front {
    left: 476px; top: 511px; width: 625px; height: 373px;
    background: var(--white);
    color: var(--navy);
  }
  .card-front .wordmark {
    position: absolute; right: 18px; top: 37px;
    color: var(--navy);
  }
  .brand-decoration {
    position: absolute; left: -20px; top: 80px; width: 280px; height: 300px;
    background: radial-gradient(ellipse at 45% 55%, var(--ghost) 0%, rgba(228,228,228,0.5) 45%, rgba(255,255,255,0) 72%);
  }
  .person-name {
    position: absolute; left: 37px; top: 203px;
    font-family: "Source Sans 3", sans-serif;
    font-weight: 700; font-size: 29px; line-height: 1;
  }
  .person-role {
    position: absolute; left: 37px; top: 241px;
    font-family: "Source Sans 3", sans-serif;
    font-weight: 300; font-size: 21px; line-height: 1;
    color: var(--muted);
  }
  .divider {
    position: absolute; left: 39px; top: 290px; width: 547px; height: 2px;
    background: var(--navy);
  }
  .contact {
    position: absolute; left: 39px; top: 307px;
    font-family: "Poppins", sans-serif;
    font-weight: 600; font-size: 16px; line-height: 23px;
    list-style: none;
  }
  .website {
    position: absolute; right: 39px; top: 333px;
    font-family: "Poppins", sans-serif;
    font-weight: 600; font-size: 16px; line-height: 1;
  }
</style>
</head>
<body>
  <section class="card card-back" role="img" aria-label="Repeating brand name pattern in dark navy on navy ground">
    <div class="wordmark">MARLOW HIRE</div>
  </section>

  <section class="card card-front">
    <div class="brand-decoration" role="img" aria-label="Faint oversized brand symbol in light grey"></div>
    <div class="wordmark">MARLOW HIRE</div>
    <h1 class="person-name">Harriet Ellison</h1>
    <p class="person-role">Director | Senior Search Consultant</p>
    <div class="divider"></div>
    <ul class="contact">
      <li class="contact-phone">+64 21 555 0147</li>
      <li class="contact-email">hello@kestrelpartners.co</li>
    </ul>
    <div class="website">marlowhire.nz</div>
  </section>
</body>
</html>
```